Coral Bay Dental Surgery Business Cards

Hi there

Can i please have a simple business card designed (front and back with a black background) using out white reverse logo and the same font used for the logo?
On the back we can just have the logo. Full details at the front part.
Here are the details:

Name of the surgery: Coral Bay | Dental Surgery
Name on the business card: Dr Owen Thackery
Credentials:
BDSc (KTL)
MSc Oral Implantology (Halvorsen, Frankfurt)
Fellow & Diplomate (Meridian Council of Restorative Prosthetics)

Email: owen.thackery@coralbaysmile.example
Address: 17 Lisgrove Rd Karrinyup
Website: coralbaysmile.example
Phone: 1800 316 482

We have attached our high res logo and a rudimentary version of the business card which is not necessarily what we want but gives all the details
We would like to have the print ready version. Thanks.

Contact Information for Business Card

website. credentials. qr code. address. phone number

Requirements
Must have
• QR code

```html
<!DOCTYPE html>
<html lang="en">
<head>
<meta charset="utf-8">
<title>Coral Bay Dental Surgery – Business Cards</title>
<link href="https://fonts.googleapis.com/css2?family=Montserrat:wght@400;500;700&display=swap" rel="stylesheet">
<style>
  :root {
    --page: #e4e6e5;
    --ink: #000000;
    --light: #e6e6e6;
    --mark: #d6d6d6;
    --text-dark: #111111;
  }
  * { margin: 0; padding: 0; box-sizing: border-box; }
  html, body { width: 1200px; height: 1200px; overflow: hidden; }
  body {
    background: var(--page);
    font-family: 'Montserrat', sans-serif;
    position: relative;
  }
  .card {
    position: absolute;
    left: 255px;
    width: 729px;
    height: 416px;
    border-radius: 5px;
    overflow: hidden;
    background: var(--ink);
  }
  .card--front { top: 134px; }
  .card--back { top: 610px; }

  /* front */
  .front-header {
    position: absolute;
    left: 62px;
    top: 50px;
    color: var(--light);
  }
  .doctor-name {
    font-weight: 700;
    font-size: 32px;
    letter-spacing: 0.2px;
    margin-bottom: 8px;
  }
  .credential {
    font-weight: 400;
    font-size: 16.5px;
    line-height: 23px;
    letter-spacing: 0.2px;
  }
  .credential--small {
    font-size: 12.5px;
    line-height: 22px;
  }
  .qr-code {
    position: absolute;
    left: 612px;
    top: 46px;
    width: 88px;
    height: 88px;
    background: var(--light);
    border-radius: 3px;
  }
  .contact-band {
    position: absolute;
    left: 0;
    top: 208px;
    width: 540px;
    height: 208px;
    background: linear-gradient(90deg, #ececec, #dedede);
    border-top-right-radius: 40px;
  }
  .contact-list {
    position: absolute;
    left: 62px;
    top: 60px;
    list-style: none;
    color: var(--text-dark);
  }
  .contact-item {
    display: flex;
    align-items: center;
    gap: 8px;
    font-size: 17px;
    line-height: 22.5px;
    letter-spacing: 0.1px;
  }
  .contact-icon { width: 14px; height: 14px; flex: none; }
  .front-mark {
    position: absolute;
    left: 540px;
    top: 208px;
    width: 189px;
    height: 208px;
    display: flex;
    flex-direction: column;
    align-items: center;
    justify-content: center;
    gap: 14px;
    color: var(--light);
    font-weight: 500;
    font-size: 15px;
    letter-spacing: 4px;
  }
  .mark-dot {
    width: 90px;
    height: 90px;
    border-radius: 50%;
    background: var(--mark);
  }

  /* back */
  .brand-dot {
    position: absolute;
    left: 176px;
    top: 136px;
    width: 144px;
    height: 144px;
    border-radius: 50%;
    background: var(--mark);
  }
  .brand {
    position: absolute;
    left: 334px;
    top: 194px;
    width: 228px;
    color: var(--light);
    font-weight: 500;
  }
  .brand-name {
    display: block;
    font-size: 20px;
    letter-spacing: 11px;
    line-height: 26px;
  }
  .brand-rule {
    display: block;
    width: 226px;
    height: 2px;
    background: var(--light);
    margin: 8px 0 9px;
  }
  .brand-sub {
    display: block;
    font-size: 20px;
    letter-spacing: 0.6px;
    line-height: 24px;
  }
</style>
</head>
<body>

<section class="card card--front">
  <div class="front-header">
    <h1 class="doctor-name">Dr Owen Thackery</h1>
    <p class="credential">BDSc (KTL)</p>
    <p class="credential">MSc Oral Implantology (Halvorsen, Frankfurt)</p>
    <p class="credential credential--small">Fellow &amp; Diplomate (Meridian Council of Restorative Prosthetics)</p>
  </div>
  <div class="qr-code" role="img" aria-label="QR code linking to the surgery website"></div>
  <div class="contact-band">
    <ul class="contact-list">
      <li class="contact-item">
        <svg class="contact-icon" viewBox="0 0 24 24"><path fill="#111" d="M6.6 10.8a15 15 0 0 0 6.6 6.6l2.2-2.2a1 1 0 0 1 1-.25 11.4 11.4 0 0 0 3.6.57 1 1 0 0 1 1 1V20a1 1 0 0 1-1 1A17 17 0 0 1 3 4a1 1 0 0 1 1-1h3.5a1 1 0 0 1 1 1c0 1.25.2 2.45.57 3.57a1 1 0 0 1-.25 1z"/></svg>
        1800 316 482
      </li>
      <li class="contact-item">
        <svg class="contact-icon" viewBox="0 0 24 24"><path fill="#111" d="M2 5h20v14H2z"/><path fill="none" stroke="#e6e6e6" stroke-width="2" d="M2 6l10 7 10-7"/></svg>
        owen.thackery@coralbaysmile.example
      </li>
      <li class="contact-item">
        <svg class="contact-icon" viewBox="0 0 24 24"><circle cx="12" cy="12" r="10" fill="none" stroke="#111" stroke-width="2"/><path fill="none" stroke="#111" stroke-width="2" d="M2 12h20M12 2c3 3 3 17 0 20M12 2c-3 3-3 17 0 20"/></svg>
        www.coralbaysmile.example
      </li>
      <li class="contact-item">
        <svg class="contact-icon" viewBox="0 0 24 24"><path fill="#111" d="M12 1a8 8 0 0 0-8 8c0 6 8 14 8 14s8-8 8-14a8 8 0 0 0-8-8zm0 11a3 3 0 1 1 0-6 3 3 0 0 1 0 6z"/></svg>
        17 Lisgrove Rd Karrinyup
      </li>
    </ul>
  </div>
  <div class="front-mark">
    <span class="mark-dot"></span>
    <span>CORAL BAY</span>
  </div>
</section>

<section class="card card--back">
  <span class="brand-dot"></span>
  <div class="brand">
    <span class="brand-name">CORAL BAY</span>
    <span class="brand-rule"></span>
    <span class="brand-sub">DENTAL SURGERY</span>
  </div>
</section>

</body>
</html>
```